Web Design Project

I'm looking for a web design that incorporates the content included below into a web site that is clearly for a platform as a service product that helps people build complex web information systems that also do mobile apps and integrations.
Updates

Project Deadline Extended
Reason: I would like to encourage more submissions so I'm extending the deadline. Designs submitted earlier may win due to immediate need for some collateral. We will be posting several other contests in the near future if this one goes well.

Here are some sample web sites we like quite a lot:

http://www.plovra.com
http://www.tarvenik.com/
http://www.tarvenik.com/skydock/ipaas-cloud-based-integration-demand
http://www.quellobarn.com/hybrid-it

It is really important that the first 5 graphic panels in the word document get translated into a rotating banner for the home page.

Our software integrates databases, services, social-media, security, and mobile devices, but it starts with building great web applications for the desktop and real integrated systems for businesses. We also integrate accounting, CRM, and lots of other things together - that's important.

We focus on creating one system. Please try to capture that concept. Don't deliver just mobile - we're system first, and mobile second. The goal is to help our customers merge all their systems into one.

Target Market(s)

CIOs, CTOs, Technical Decision Makers, Business People

Industry/Entity Type

Build

Requirements
Must have
• Home Page that introduces the product and what it can do for people. Product Page that shows options for the product: Platform as a Service and Licensing. Services page that shows options for Services - Virtual Development Teams and Professional Services. A Blog Page. About Us Page with location info, contact info, etc.
Nice to have
• Scrolling home page banners. Lead generation - Contact us form.

```html
<!DOCTYPE html>
<html lang="en">
<head>
<meta charset="utf-8">
<title>Emberline Technologies</title>
<link rel="stylesheet" href="https://fonts.googleapis.com/css2?family=Bitter:wght@400;700&family=Arimo:wght@400;700&family=Open+Sans:ital,wght@0,400;0,600;1,400;1,600&family=Ubuntu:wght@500;700&display=swap">
<style>
  :root {
    --ink: #2a2a2a;
    --body: #3a3a3a;
    --muted: #6a6a6a;
    --orange: #ef8a3a;
    --red: #d42a1e;
    --red-dark: #a8160e;
    --blue: #1e8ac8;
    --green: #9cc623;
    --nav-grey: #7a7a7a;
    --card-bg: #f2f2f2;
    --card-line: #dddddd;
    --footer: #2b2b2b;
    --footer-text: #ffffff;
    --sky-top: #8ec8f0;
    --sky-bottom: #ffffff;
  }
  * { margin: 0; padding: 0; box-sizing: border-box; }
  html, body { width: 960px; height: 1200px; overflow: hidden; }
  body { position: relative; background: #fff; font-family: "Arimo", Arial, sans-serif; color: var(--body); }
  .abs { position: absolute; }

  /* header */
  .site-header { left: 0; top: 0; width: 960px; height: 83px; background: linear-gradient(#ffffff, #f3f3f3); border-bottom: 1px solid #e2e2e2; }
  .brand { left: 98px; top: 20px; display: flex; align-items: center; gap: 8px; }
  .brand-mark { width: 30px; height: 30px; border-radius: 50%; background: var(--orange); }
  .brand-name { font-family: "Ubuntu", sans-serif; font-weight: 700; font-size: 22px; color: #555; letter-spacing: .5px; }
  .social-top { left: 724px; top: 8px; display: flex; gap: 14px; }
  .social-top span { width: 28px; height: 28px; border-radius: 50%; background: var(--c); display: block; }
  .main-nav { left: 442px; top: 50px; font-family: "Open Sans", sans-serif; font-weight: 600; font-size: 11px; color: var(--nav-grey); }
  .main-nav a { text-decoration: none; color: inherit; position: absolute; top: 5px; white-space: nowrap; }
  .main-nav .active { left: 0; top: 0; width: 90px; height: 23px; border-radius: 12px; background: linear-gradient(#9a9a9a, #6e6e6e); color: #fff; text-align: center; line-height: 23px; box-shadow: inset 0 1px 2px rgba(0,0,0,.3); }

  /* hero */
  .hero { left: 0; top: 84px; width: 960px; height: 330px; background: linear-gradient(var(--sky-top) 0%, #c8e4f8 55%, var(--sky-bottom) 100%); }
  .hero-title { left: 102px; top: 24px; width: 430px; font-family: "Bitter", serif; font-weight: 400; font-size: 29px; line-height: 39px; color: var(--ink); }
  .hero-title .hl { color: var(--orange); font-weight: 700; }
  .hero-title .strong { color: var(--red); font-weight: 700; }
  .hero-copy { left: 102px; top: 152px; width: 424px; font-size: 10.6px; line-height: 14.4px; color: #222; }
  .btn-profile { left: 105px; top: 239px; width: 190px; height: 35px; border-radius: 5px; background: linear-gradient(#f06a3a, #d23a1c); border: 1px solid #b52a12; color: #fff; font-family: "Ubuntu", sans-serif; font-weight: 700; font-size: 14px; text-align: center; line-height: 33px; letter-spacing: .4px; }
  .btn-shadow { left: 135px; top: 282px; width: 120px; height: 8px; border-radius: 50%; background: radial-gradient(rgba(0,0,0,.35), rgba(0,0,0,0) 70%); }
  .slide-arrow { width: 42px; height: 42px; border-radius: 50%; display: flex; align-items: center; justify-content: center; }
  .slide-arrow.prev { left: 22px; top: 128px; background: #111; }
  .slide-arrow.next { left: 890px; top: 128px; background: #c9ccd0; }
  .hero-devices { left: 576px; top: 20px; width: 284px; height: 272px; background: linear-gradient(#c9d6e0, #aebbc5); }

  /* feature cards */
  .card { top: 418px; width: 235px; height: 247px; background: linear-gradient(#ffffff, var(--card-bg)); border: 1px solid var(--card-line); text-align: center; }
  .card h2 { margin-top: 12px; font-family: "Bitter", serif; font-weight: 700; font-size: 19px; color: var(--ink); }
  .card .art { margin: 14px auto 0; width: 152px; height: 82px; border-radius: 40px; background: radial-gradient(#d9e6f2, #eef2f6 70%); }
  .card p { margin: 12px auto 0; width: 212px; font-size: 9.8px; line-height: 14.4px; color: #555; }
  .readmore { display: inline-block; margin-top: 8px; width: 77px; height: 24px; border-radius: 12px; background: linear-gradient(#e8301e, #c31608); border: 2px solid #fff; box-shadow: 0 0 0 1px var(--red-dark); color: #fff; font-weight: 700; font-size: 10.4px; line-height: 20px; }

  /* welcome */
  .welcome-mark { left: 88px; top: 724px; width: 40px; height: 40px; border-radius: 50%; background: var(--orange); }
  .welcome-title { left: 142px; top: 729px; font-family: "Bitter", serif; font-weight: 400; font-size: 20px; color: #444; }
  .welcome-title b { color: var(--red); font-weight: 700; }
  .welcome-art { left: 94px; top: 776px; width: 136px; height: 112px; background: linear-gradient(#eef4f8, #d8e6ef); border-radius: 4px; }
  .welcome-copy { left: 244px; top: 768px; width: 364px; font-family: "Open Sans", sans-serif; font-size: 8.6px; line-height: 14.4px; color: #666; text-align: justify; }
  .welcome-copy em { font-weight: 600; color: #333; }
  .welcome-copy p + p { margin-top: 14px; }

  /* testimonials */
  .testi-art { left: 660px; top: 708px; width: 40px; height: 32px; border-radius: 4px; background: linear-gradient(#dfe4e8, #b9c1c7); }
  .testi-title { left: 704px; top: 716px; font-family: "Ubuntu", sans-serif; font-weight: 500; font-size: 17.5px; color: var(--blue); }
  .testi-quote { left: 658px; top: 752px; width: 198px; font-family: "Open Sans", sans-serif; font-size: 9.4px; line-height: 16px; color: #444; text-align: justify; }
  .qmark { font-family: "Bitter", serif; font-size: 28px; color: #999; line-height: 1; }
  .qmark.open { left: 638px; top: 748px; }
  .qmark.close { left: 844px; top: 850px; }
  .testi-name { left: 661px; top: 874px; font-family: "Open Sans", sans-serif; font-style: italic; font-size: 11.5px; color: #444; }
  .testi-rule { left: 654px; top: 902px; width: 220px; height: 1px; background: #d6d6d6; }

  /* call to action */
  .cta-band { left: 0; top: 944px; width: 960px; height: 82px; background: linear-gradient(90deg, #fff, #f3f4f4 20%, #f3f4f4 80%, #fff); }
  .cta-text { left: 110px; top: 968px; font-family: "Ubuntu", sans-serif; font-weight: 700; font-size: 29px; color: var(--green); }
  .cta-arrow { left: 608px; top: 977px; }
  .cta-button { left: 661px; top: 964px; width: 179px; height: 46px; background: linear-gradient(#ffffff, #eeeeee); border: 1px solid #d4d4d4; border-left: 5px solid #c7e021; box-shadow: 0 3px 5px rgba(0,0,0,.15); font-family: "Ubuntu", sans-serif; font-weight: 700; font-size: 16.5px; color: var(--blue); text-align: center; line-height: 44px; }

  /* newsletter */
  .newsletter { left: 94px; top: 1047px; width: 756px; height: 40px; border: 1px solid #c8d2d6; border-radius: 3px; background: linear-gradient(#f4f7f8, #e3eaed); }
  .newsletter-icon { left: 0; top: 0; width: 50px; height: 38px; background: #cfd9dd; display: flex; align-items: center; justify-content: center; }
  .newsletter-text { left: 65px; top: 12px; font-family: "Bitter", serif; font-size: 11.4px; color: #444; }
  .newsletter-input { left: 492px; top: 8px; width: 180px; height: 22px; border-radius: 6px; background: #fff; border: 1px solid #d0d0d0; }
  .newsletter-submit { left: 677px; top: 8px; width: 63px; height: 22px; border-radius: 4px; background: linear-gradient(#9aa2a6, #6b7378); color: #fff; font-size: 10px; text-align: center; line-height: 22px; }

  /* footer */
  .site-footer { left: 0; top: 1112px; width: 960px; height: 88px; background: var(--footer); }
  .footer-brand { left: 86px; top: 24px; display: flex; align-items: center; gap: 8px; }
  .footer-brand .brand-mark { background: #8a8a8a; }
  .footer-brand .brand-name { color: #bdbdbd; }
  .footer-nav { left: 300px; top: 34px; width: 416px; text-align: center; font-size: 10.2px; color: var(--footer-text); word-spacing: 2px; }
  .footer-copy { left: 300px; top: 53px; width: 416px; text-align: center; font-size: 10.2px; color: var(--footer-text); }
  .follow { left: 772px; top: 27px; font-size: 8.8px; color: #9a9a9a; }
  .follow-icons { left: 770px; top: 46px; display: flex; gap: 8px; }
  .follow-icons span { width: 17px; height: 17px; background: #8c8c8c; border-radius: 2px; display: block; }
</style>
</head>
<body>

<header class="site-header abs">
  <div class="brand abs"><span class="brand-mark"></span><span class="brand-name">EMBERLINE</span></div>
  <div class="social-top abs" aria-label="Social links">
    <span style="--c:#3b5fa8"></span><span style="--c:#c9c9c9"></span><span style="--c:#3fb0e2"></span><span style="--c:#ee6a1f"></span>
  </div>
  <nav class="main-nav abs">
    <a class="active" href="#">Home</a>
    <a href="#" style="left:108px">Platform</a>
    <a href="#" style="left:202px">Services</a>
    <a href="#" style="left:296px">Blog</a>
    <a href="#" style="left:369px">About Us</a>
  </nav>
</header>

<section class="hero abs">
  <h1 class="hero-title abs">The <span class="hl">power of off-the-</span><br>shelf; the capabilitytodo-it-<br><span class="strong">YOURSELF</span></h1>
  <p class="hero-copy abs">Lorem Ipsum is simply dummy text of the printing and typesetting industry. Lorem Ipsum has been the industry's standard dummy text ever since the 1500s, when an unknown printer took a galley of type and scrambled it to make a type specimen book. It has survived not only five centuries, but also the leap into electronic typesetting,</p>
  <div class="btn-profile abs">Read Company Profile</div>
  <div class="btn-shadow abs"></div>
  <div class="slide-arrow prev abs"><svg width="14" height="16" viewBox="0 0 14 16"><path d="M12 1 L2 8 L12 15 Z" fill="#fff"/></svg></div>
  <div class="slide-arrow next abs"><svg width="14" height="16" viewBox="0 0 14 16"><path d="M2 1 L12 8 L2 15 Z" fill="#fff"/></svg></div>
  <div class="hero-devices abs" role="img" aria-label="Product image: tablet and two phones running the platform's apps"></div>
</section>

<article class="card abs" style="left:96px">
  <h2>Introduction</h2>
  <div class="art" role="img" aria-label="Cloud made of many small app and service icons"></div>
  <p>Lorem Ipsum is simply dummy text of the printing and typesetting industry. Lorem Ipsum has been the industry's standard dummy text ever since the 1500s, when an unknown...</p>
  <span class="readmore">Readmore</span>
</article>
<article class="card abs" style="left:354px">
  <h2>One Business</h2>
  <div class="art" role="img" aria-label="Hub diagram linking a central database to many services"></div>
  <p>Lorem Ipsum is simply dummy text of the printing and typesetting industry. Lorem Ipsum has been the industry's standard dummy text ever since the 1500s, when an unknown...</p>
  <span class="readmore">Readmore</span>
</article>
<article class="card abs" style="left:612px">
  <h2 style="margin-top:10px">One Development</h2>
  <div class="art" role="img" aria-label="Network diagram of connected devices and team members"></div>
  <p>Lorem Ipsum is simply dummy text of the printing and typesetting industry. Lorem Ipsum has been the industry's standard dummy text ever since the 1500s, when an unknown...</p>
  <span class="readmore">Readmore</span>
</article>

<div class="welcome-mark abs"></div>
<h2 class="welcome-title abs">Welcome to the <b>Emberline</b></h2>
<div class="welcome-art abs" role="img" aria-label="Illustrated businessman presenting a rising chart"></div>
<div class="welcome-copy abs">
  <p><em>Lorem Ipsum is simply dummy text of the printing and typesetting industry. Lorem Ipsum has been the industry's standard dummy text ever since the 1500s,</em> when an unknown printer took a galley of type and scrambled it to make a type specimen book. It has survived not only five centuries, but also the leap.</p>
  <p>It was popularised in the 1960s with the release of Lettrane sheets containing Lorem Ipsum passages, and more recently with desktop publishing software like Orvel PageSet including versions of Lorem Ipsum.</p>
</div>

<div class="testi-art abs" role="img" aria-label="Small figure with speech bubble"></div>
<h2 class="testi-title abs">TESTIMONIALS</h2>
<span class="qmark open abs">&ldquo;</span>
<p class="testi-quote abs">Lorem Ipsum is simply dummy text of the printing and typesetting industry. Lorem Ipsum has been the industry's standard dummy text ever since the 1500s, when an unknown printer took a galley of type and scrambled it to make a type specimen book. It has survived not only five centuries.</p>
<span class="qmark close abs">&rdquo;</span>
<span class="testi-name abs">Dana Whitcombe</span>
<div class="testi-rule abs"></div>

<section class="cta-band abs"></section>
<p class="cta-text abs">Pointing You in the Right Direction!</p>
<svg class="cta-arrow abs" width="32" height="22" viewBox="0 0 32 22"><path d="M0 6 H18 V0 L32 11 L18 22 V16 H0 Z" fill="#1877c2"/></svg>
<div class="cta-button abs">Get Started Now</div>

<form class="newsletter abs">
  <div class="newsletter-icon abs"><svg width="30" height="22" viewBox="0 0 30 22"><rect x="1" y="1" width="28" height="20" fill="#fff" stroke="#111" stroke-width="2"/><path d="M1 1 L15 13 L29 1 M1 21 L11 10 M29 21 L19 10" fill="none" stroke="#111" stroke-width="2"/></svg></div>
  <span class="newsletter-text abs">Enter your email valid address to subscribe our Monthly Newsletter</span>
  <div class="newsletter-input abs"></div>
  <div class="newsletter-submit abs">Submit</div>
</form>

<footer class="site-footer abs">
  <div class="footer-brand abs"><span class="brand-mark"></span><span class="brand-name">EMBERLINE</span></div>
  <p class="footer-nav abs">Home &nbsp;~&nbsp; Platform &nbsp;~&nbsp; Services &nbsp;~&nbsp; Blog &nbsp;~&nbsp; About Us</p>
  <p class="footer-copy abs">Copyright © 2013 emberline. All right reserved</p>
  <p class="follow abs">Follow us here:</p>
  <div class="follow-icons abs"><span></span><span></span><span></span><span></span></div>
</footer>

</body>
</html>
```